Software Product Flyer Design

A established czech software company needs a marketing flyer to promote their software product and its modules.
The overall feel of the flyer must to be serious, but also eye-catching, enticing, clever and bold to attract customers.
Unifying graphic element is the new product logo.
The flyer would be A4, colour both sides and folded once (to give 4 pages of A5).
Title page - product logo with module name and module icon, short presentation of the product and list of its key features.
Inside pages - detailed informations with screenshots or graphical schemas.
Back side - informations about technical requirements and user support, contacts (address, phone, fax, e-mail, web pages - no social networks).
Product logo, module icon and some images attached.
Updates
Hello,
Reason: For organizational reasons we extending the deadline by 10 days.
FYI: We have uploaded the new ZIP file with previous version of our flyer.
Attached PDF file with text for inner pages.
Target Market(s)
Existing or new customers like municipalities, public authorities and nonprofit organizations.
Industry/Entity Type
Marketing
Requirements
Must have
- Winning designer must provide a template for Adobe InDesign based on his graphic design.
Avoid to using exotic fonts - in Czech we use Latin Extended characters (like áéěíýůčřžšťďň).
Nice to have
- Using graphic motif from product logo like as attached splash screen.

```html
<!DOCTYPE html>
<html lang="cs">
<head>
<meta charset="utf-8">
<title>Nexora – Majetek, leták</title>
<link href="https://fonts.googleapis.com/css2?family=Open+Sans:ital,wght@0,400;0,600;0,700;0,800;1,400&family=Archivo+Black&display=swap" rel="stylesheet">
<style>
:root{
  --slate:#40464e;
  --slate-dark:#353a41;
  --orange:#f0641e;
  --paper:#f4f4f4;
  --paper-shade:#e4e5e6;
  --ink:#222;
  --muted:#6a6f75;
  --screen:#c9d2d8;
  --backdrop:#d9d6d1;
}
*{box-sizing:border-box;margin:0;padding:0}
html,body{width:1200px;height:1200px;overflow:hidden}
body{background:var(--backdrop);font-family:"Open Sans",Arial,sans-serif;color:var(--ink);position:relative}
.spread{position:absolute;left:220px;width:760px;height:537px;display:flex;box-shadow:0 6px 18px rgba(0,0,0,.25)}
.spread--outer{top:42px}
.spread--inner{top:621px}
.page{position:relative;width:380px;height:537px;overflow:hidden;background:linear-gradient(90deg,var(--paper-shade),var(--paper) 30%,#fff)}
.page--left{background:linear-gradient(270deg,var(--paper-shade),var(--paper) 25%,#fff)}
.abs{position:absolute}
.brand{font-family:"Open Sans",sans-serif;font-weight:800;color:var(--slate);display:flex;align-items:center;gap:5px;letter-spacing:-.5px;white-space:nowrap}
.brand__dot{width:.6em;height:.6em;border-radius:50%;background:var(--orange)}
.shot{background:linear-gradient(180deg,#eef2f5,var(--screen));border:2px solid #fff}
.lorem{font-size:7.2px;line-height:1.35;text-align:justify}
.title{font-weight:700;font-size:10px}
.subtitle{font-style:italic;font-size:6px;color:#aaa}
/* back page */
.back__top{left:0;top:0;width:310px;height:250px;background:var(--slate);color:#fff}
.back__heading{left:110px;top:8px;font-size:11px;font-weight:600}
.back__intro{left:110px;top:24px;width:190px;font-size:5.6px;line-height:1.3}
.back__server{left:96px;top:48px;width:14px;height:72px;background:var(--orange);writing-mode:vertical-rl;transform:rotate(180deg);font-size:7px;font-weight:700;text-align:center;line-height:14px}
.back__shot{left:14px;top:48px;width:80px;height:72px}
.bullets{list-style:none;font-size:5.6px;line-height:1.35}
.bullets li{position:relative;padding-left:8px;margin-bottom:3px}
.bullets li::before{content:"";position:absolute;left:1px;top:2px;width:3px;height:3px;border-radius:50%;background:currentColor}
.back__server-list{left:118px;top:50px;width:185px}
.back__bar{left:0;top:128px;width:310px;height:14px;background:var(--orange);font-size:9px;font-weight:700;padding-left:14px;line-height:14px}
.back__station-list{left:14px;top:148px;width:290px}
.back__support{left:14px;top:262px;width:290px;text-align:center}
.back__support h3{color:var(--orange);font-size:11px;font-weight:700;margin-bottom:4px}
.back__support p{font-size:6.2px;line-height:1.35;margin-bottom:8px}
.back__support ul{list-style:none;font-size:5.6px;line-height:1.45;font-style:italic;color:#333}
.back__logo{left:80px;top:410px;font-size:26px}
.back__contact{left:40px;top:448px;width:240px;text-align:center;font-size:6px;line-height:1.4;font-style:normal}
.back__stripe{left:0;bottom:18px;width:310px;height:4px;background:var(--orange)}
.back__strip{right:0;top:0;width:70px;height:100%;background:var(--slate)}
.back__strip .shot{position:absolute;left:8px;width:54px;height:44px}
/* front page */
.front__strip{left:0;top:0;width:36px;height:100%;background:var(--slate)}
.front__logo{left:60px;top:40px;font-size:38px}
.front__icon{right:30px;top:100px;width:18px;height:18px;border:1.5px solid var(--slate);background:#fff;font-size:10px;font-weight:700;text-align:center;line-height:15px;color:var(--slate)}
.front__module{right:28px;top:124px;font-family:"Archivo Black",sans-serif;font-size:24px;color:var(--slate);letter-spacing:1px}
.front__intro{left:170px;top:168px;width:180px;color:var(--orange);font-size:8.6px;line-height:1.3;text-align:justify}
.front__benefits{left:110px;top:400px;width:250px}
.front__benefits h3{font-size:12px;font-weight:700;color:var(--ink);display:flex;align-items:center;gap:10px}
.front__benefits-icon{width:14px;height:18px;background:linear-gradient(var(--orange),#b9601e);border-radius:3px}
.front__rule{height:2px;background:var(--orange);margin:4px 0}
.front__features{list-style:none;font-size:9px;font-weight:700;line-height:1.3}
.front__features li::before{content:"▶ ";font-size:7px}
/* inner left */
.il__shot{left:22px;top:20px;width:190px;height:150px}
.il__review{left:225px;top:14px;width:140px;height:508px;background:var(--slate);color:#fff}
.il__review-head{right:8px;top:6px;font-size:11px}
.il__reviewer{left:12px;top:30px;font-size:7px;font-weight:700;line-height:1.3}
.il__image{left:14px;top:54px;width:110px;height:90px;background:#9a9ea3;color:#e8e8e8;font-weight:800;font-size:20px;display:flex;align-items:center;justify-content:center}
.il__quote{left:14px;top:156px;width:112px;font-size:7.4px;line-height:1.45;color:#eee}
.il__title{left:22px;top:182px}
.il__text{left:22px;top:198px;width:190px}
.il__cols{left:22px;top:280px;width:190px;display:flex;gap:10px}
.il__cols .lorem{flex:1}
.il__logo{left:22px;top:496px;font-size:18px}
.il__rule{left:112px;top:509px;width:100px;height:1px;background:#aaa}
/* inner right */
.ir__panel{left:12px;top:14px;width:356px;height:174px;background:var(--slate);color:#fff}
.ir__shot{left:10px;top:20px;width:150px;height:130px}
.ir__title{left:172px;top:20px;color:#fff}
.ir__sub{left:172px;top:33px}
.ir__quote{left:172px;top:48px;width:174px;font-size:6.8px;line-height:1.4;color:#eee;text-align:justify}
.ir__t2{left:20px;top:200px}
.ir__text{left:20px;top:216px;width:230px}
.ir__side{left:262px;top:196px;width:106px;height:148px;background:var(--slate);color:#fff}
.ir__side .title{position:absolute;left:8px;top:8px;font-size:9px}
.ir__side .subtitle{position:absolute;left:8px;top:21px}
.ir__side .lorem{position:absolute;left:8px;top:34px;width:90px;color:#eee;text-align:left;font-size:6.8px}
.ir__strip{left:20px;top:372px;width:240px;height:70px}
.ir__quote2{left:270px;top:352px;width:98px;font-size:6.8px;line-height:1.35}
.ir__logo{right:14px;top:440px;font-size:18px}
</style>
</head>
<body>

<section class="spread spread--outer">
  <article class="page page--left back">
    <div class="abs back__top">
      <div class="abs back__heading">Technické podmínky</div>
      <p class="abs back__intro">Systém Nexora umožňuje nasazení prakticky u jakéhokoli zákazníka v jakémkoli prostředí bez ohledu na počet uživatelů nebo množství dat.</p>
      <div class="abs shot back__shot" role="img" aria-label="Snímek obrazovky aplikace s tabulkou dat"></div>
      <div class="abs back__server">SERVER</div>
      <ul class="abs bullets back__server-list">
        <li>Operační systém Fenix OS 7 a novější nebo operační systém Lumen OS</li>
        <li>Systém vyžaduje nainstalovaný runtime pro Kava 1.7, databázi BaseQL ve verzi 9.2, webový server Harbor Server 7.0 a systém QueueLine</li>
        <li>Doporučená velikost RAM je minimálně 4 GB</li>
        <li>Minimální disková velikost je 20 GB</li>
      </ul>
      <div class="abs back__bar">Pracovní stanice</div>
      <ul class="abs bullets back__station-list">
        <li>Operační systém Fenix OS 7 a novější</li>
        <li>Minimální velikost RAM je 2 GB</li>
        <li>Minimální diskový prostor je 5 GB</li>
        <li>Pro běh programu Nexora na pracovní stanici je zapotřebí runtime pro Kava 1.7 (je součástí instalace)</li>
        <li>Pro zobrazení a tisk sestav je zapotřebí prohlížeč PDF souborů (Papyr Reader X nebo jiný)</li>
        <li>Podporované kancelářské balíky: Tabula Office 2007 a novější, Libra Office 3.0 a novější, Aperta Office 3.0 a novější</li>
      </ul>
    </div>
    <div class="abs back__support">
      <h3>Uživatelská podpora</h3>
      <p>Společnost Veltis si zakládá na důvěrném vztahu se zákazníky, který se podařilo za více než 20 let existence firmy vybudovat.</p>
      <ul>
        <li>Regionální zastoupení po celé České republice</li>
        <li>Individuální přístup ke každému zákazníkovi</li>
        <li>Pracovní postupy zpracované formou názorných prezentací</li>
        <li>Tichá aktualizace programů přes internet</li>
        <li>Školení, metodická podpora a telefonické poradenství</li>
        <li>Aktuální informace na webových stránkách</li>
      </ul>
    </div>
    <div class="abs brand back__logo"><span class="brand__dot"></span>Nexora</div>
    <address class="abs back__contact">
      NEXORA LTD<br>
      48 Linden Row, Brno, Suite 3<br>
      Email : info@nexorasoft.example, Website : www.nexorasoft.example<br>
      Phone : 1234567890 , Fax : 1234567890
    </address>
    <div class="abs back__stripe"></div>
    <div class="abs back__strip">
      <div class="shot" style="top:120px" role="img" aria-label="Snímek obrazovky – přehled"></div>
      <div class="shot" style="top:180px" role="img" aria-label="Snímek obrazovky – seznam"></div>
      <div class="shot" style="top:240px" role="img" aria-label="Snímek obrazovky – formulář"></div>
      <div class="shot" style="top:300px" role="img" aria-label="Snímek obrazovky – okno aplikace"></div>
    </div>
  </article>

  <article class="page front">
    <div class="abs front__strip"></div>
    <div class="abs brand front__logo"><span class="brand__dot"></span>Nexora</div>
    <div class="abs front__icon" role="img" aria-label="Ikona modulu Majetek">A</div>
    <h1 class="abs front__module">MAJETEK</h1>
    <p class="abs front__intro">Lorem ipsum dolor sit amet, consectetur adipisicing elit, sed do eiusmod tempor incididunt ut labore et dolore magna aliqua. Ut enim ad minim veniam, quis nostrud exercitation ullamco laboris nisi ut aliquip ex ea commodo consequat.</p>
    <div class="abs front__benefits">
      <h3>Co vam prinese <span class="front__benefits-icon" role="img" aria-label="Ilustrace modulu"></span></h3>
      <div class="front__rule"></div>
      <ul class="front__features">
        <li>Here will go key feature</li>
        <li>Here will go key feature</li>
        <li>Here will go key feature</li>
        <li>Here will go key feature</li>
      </ul>
      <div class="front__rule"></div>
    </div>
  </article>
</section>

<section class="spread spread--inner">
  <article class="page page--left inner-left">
    <div class="abs shot il__shot" role="img" aria-label="Snímek obrazovky aplikace se seznamem majetku"></div>
    <h2 class="abs title il__title">Title Of the Topic</h2>
    <p class="abs lorem il__text">"Lorem ipsum dolor sit amet, consectetur adipisicing elit, sed do eiusmod tempor incididunt ut labore et dolore magna aliqua. Ut enim ad minim veniam, quis nostrud exercitation ullamco laboris nisi ut aliquip ex ea commodo consequat. Duis aute irure dolor in reprehenderit in voluptate velit esse cillum dolore eu fugiat nulla pariatur.</p>
    <div class="abs il__cols">
      <p class="lorem">"Lorem ipsum dolor sit amet, consectetur adipisicing elit, sed do eiusmod tempor incididunt ut labore et dolore magna aliqua. Ut enim ad minim veniam, quis nostrud exercitation ullamco laboris nisi ut aliquip ex ea commodo consequat. Duis aute irure dolor in reprehenderit in voluptate velit esse cillum dolore eu fugiat nulla pariatur."</p>
      <p class="lorem">"Lorem ipsum dolor sit amet, consectetur adipisicing elit, sed do eiusmod tempor incididunt ut labore et dolore magna aliqua. Ut enim ad minim veniam, quis nostrud exercitation ullamco laboris nisi ut aliquip ex ea commodo consequat. Duis aute irure dolor in reprehenderit in voluptate velit esse cillum dolore eu fugiat nulla pariatur.</p>
    </div>
    <div class="abs il__review">
      <div class="abs il__review-head">Review</div>
      <div class="abs il__reviewer">Reviewer Name<br>Rank# 1</div>
      <div class="abs il__image" role="img" aria-label="Fotografie recenzenta">Image</div>
      <p class="abs il__quote">"Lorem ipsum dolor sit amet, consectetur adipisicing elit, sed do eiusmod tempor incididunt ut labore et dolore magna aliqua. Ut enim ad minim veniam, quis nostrud exercitation ullamco laboris nisi ut aliquip ex ea commodo consequat. Duis aute irure dolor in reprehenderit in voluptate velit esse cillum dolore eu fugiat nulla pariatur. Excepteur sint occaecat cupidatat non proident, sunt in culpa qui officia deserunt mollit anim id est laborum."</p>
    </div>
    <div class="abs brand il__logo"><span class="brand__dot"></span>Nexora</div>
    <div class="abs il__rule"></div>
  </article>

  <article class="page inner-right">
    <div class="abs ir__panel">
      <div class="abs shot ir__shot" role="img" aria-label="Snímek obrazovky s formulářem karty majetku"></div>
      <h2 class="abs title ir__title">Title Of the Topic</h2>
      <div class="abs subtitle ir__sub">Any Subtitle will go here</div>
      <p class="abs ir__quote">"Lorem ipsum dolor sit amet, consectetur adipisicing elit, sed do eiusmod tempor incididunt ut labore et dolore magna aliqua. Ut enim ad minim veniam, quis nostrud exercitation ullamco laboris nisi ut aliquip ex ea commodo consequat. Duis aute irure dolor in reprehenderit in voluptate velit esse cillum dolore eu fugiat nulla pariatur. Excepteur sint occaecat cupidatat non proident, sunt in culpa qui officia deserunt mollit anim id est laborum."</p>
    </div>
    <h2 class="abs title ir__t2">Title Of the Topic</h2>
    <div class="abs ir__text">
      <p class="lorem">"Lorem ipsum dolor sit amet, consectetur adipisicing elit, sed do eiusmod tempor incididunt ut labore et dolore magna aliqua. Ut enim ad minim veniam, quis nostrud exercitation ullamco laboris nisi ut aliquip ex ea commodo consequat. Duis aute irure dolor in reprehenderit in voluptate velit esse cillum dolore eu fugiat nulla pariatur.</p>
      <p class="lorem" style="margin-top:8px">"Lorem ipsum dolor sit amet, consectetur adipisicing elit, sed do eiusmod tempor incididunt ut labore et dolore magna aliqua. Ut enim ad minim veniam, quis nostrud exercitation ullamco laboris nisi ut aliquip ex ea commodo consequat. Duis aute irure dolor in reprehenderit in voluptate velit esse cillum dolore eu fugiat nulla pariatur.</p>
    </div>
    <aside class="abs ir__side">
      <h2 class="title">Title Of the Topic</h2>
      <div class="subtitle">Any Subtitle will go here</div>
      <p class="lorem">"Lorem ipsum dolor sit amet, consectetur adipisicing elit, sed do eiusmod tempor incididunt ut labore et dolore magna aliqua. Ut enim ad minim veniam, quis nostrud exercitation ullamco laboris nisi ut aliquip ex ea commodo consequat."</p>
    </aside>
    <div class="abs shot ir__strip" role="img" aria-label="Snímek obrazovky s hlavní nabídkou modulů"></div>
    <p class="abs ir__quote2">"Lorem ipsum dolor sit amet, consectetur adipisicing elit, sed do eiusmod tempor incididunt ut labore et dolore magna aliqua.</p>
    <div class="abs brand ir__logo"><span class="brand__dot"></span>Nexora</div>
  </article>
</section>

</body>
</html>
```